Résumé app needs 1 more template

Hi, I need 1 more template for my résumé app. The résumé app can be used in a browser (https://paperloom.com/resume-app) on an Nexor / Tabbo (https://apps.marlowstore.com/app/id530218746) or on an Veltrix (https://get.brinkmarket.com/store/apps/details?id=com.paperloom.resume). The app lets the user create a résumé. It currently let's the user choose between 3 templates. I need 1 more. Please use the app first so you know how it will work.

Target Market(s)

Users of the app

Colors

Requirements
Must have
• original
• beautiful
• the resume template contains the data that the user can currently enter in the app (so do NOT design new features like sliders for level of experience etc)

```html
<!DOCTYPE html>
<html lang="en">
<head>
<meta charset="utf-8">
<title>Résumé template</title>
<link rel="stylesheet" href="https://fonts.googleapis.com/css2?family=Open+Sans:ital,wght@0,400;0,600;0,700;1,400&display=swap">
<style>
:root{
  --wine:#6c0b12;
  --wine-text:#7a1018;
  --ink:#1c1c1c;
  --paper:#ffffff;
  --rule:#c9c9c9;
  --block:#d9d9d9;
}
*{margin:0;padding:0;box-sizing:border-box}
html,body{width:848px;height:1200px;overflow:hidden;background:var(--paper)}
body{font-family:"Open Sans",Arial,sans-serif;color:var(--ink);position:relative}
.sidebar{position:absolute;left:0;top:0;width:267px;height:1200px;background:var(--wine);color:var(--paper)}
.portrait-ring{position:absolute;left:24px;top:8px;width:276px;height:276px;border-radius:50%;border:2px solid var(--paper);background:var(--wine);z-index:2}
.portrait{position:absolute;left:10px;top:10px;width:252px;height:252px;border-radius:50%;background:radial-gradient(circle at 50% 40%,#b8b8b8,#5a5a5a 60%,#262626)}
.side-title{position:absolute;left:20px;font-size:25px;font-weight:400;letter-spacing:.5px}
.side-text{position:absolute;left:20px;width:214px;font-size:16px;line-height:21px;hyphens:auto;-webkit-hyphens:auto}
.side-text p+p{margin-top:21px}
.contact{position:absolute;left:20px;top:992px;font-size:18px;line-height:23px}
.header{position:absolute;left:267px;top:0;width:571px;height:172px;background:var(--wine);color:var(--paper);text-align:center}
.header .topline{position:absolute;left:0;right:0;top:19px;height:2px;background:var(--paper)}
.name{position:absolute;left:0;right:0;top:46px;font-size:43px;font-weight:700;line-height:1}
.profession{position:absolute;left:0;right:0;top:101px;font-size:24px;font-style:italic}
.contact-line{position:absolute;left:0;right:0;top:142px;font-size:18px;padding-left:60px}
.contact-line span+span{margin-left:22px}
.rule-h{position:absolute;left:300px;width:538px;height:2px;background:var(--wine)}
.frame-left{position:absolute;left:268px;top:172px;width:1px;height:1028px;background:var(--rule)}
.frame-right{position:absolute;left:837px;top:172px;width:1px;height:1028px;background:var(--rule)}
.section-icon{position:absolute;left:302px;width:40px;height:36px}
.section-title{position:absolute;left:388px;width:450px;font-size:25px;font-weight:400;border-bottom:1.5px solid var(--wine);padding-bottom:1px;line-height:34px}
.entry{position:absolute;left:284px;width:544px}
.entry .dates{position:absolute;left:0;top:0;width:84px;text-align:right;font-size:16px}
.entry .body{margin-left:104px}
.entry .title{color:var(--wine-text);font-weight:600;font-size:16.5px;line-height:22px}
.entry .org{font-size:16px;line-height:21px}
.entry .school{font-style:italic;font-size:16px;line-height:21px}
.entry .label{font-size:16px;line-height:21px}
.entry .desc-label{font-style:italic;font-size:16px;line-height:21px;margin-top:16px}
.entry .desc{font-size:13.5px;line-height:16.5px;width:440px;text-align:justify;hyphens:auto;-webkit-hyphens:auto}
.company-block{position:absolute;right:14px;top:14px;width:76px;height:36px;background:var(--block)}
.extra{position:absolute;left:388px;top:1098px;list-style:none;font-size:13.5px;line-height:17px}
.extra li::before{content:"·"}
</style>
</head>
<body>
<aside class="sidebar">
  <h2 class="side-title" style="top:302px">ABOUT YOU</h2>
  <div class="side-text" style="top:349px">
    <p>Lorem ipsum dolor sit amet, consectetur adipiscing elit. Proin gravida purus justo, sit amet ultricies turpis aliquam eget. Suspendisse iaculis, lectus at consectetur iaculis, urna ligula imperdiet nisl, a mattis massa.</p>
    <p>Cras erat mauris, convallis vel gravida eu, ultrices vel odio. Maecenas et vulputate est. Donec mattis, eros eu rhoncus placerat, mi augue faucibus leo, at finibus ipsum est et libero. Nam velit dolor, lacinia at elit a, blandit condimentum lorem. Etiam dapibus pretium posuere. Nullam varius nisi a libero pellentesque ultrices. Integer euismod, tellus at mattis vs aliquam. Ut auctor tellus eu tortor posuere, vitae finibus dolor laoreet.</p>
  </div>
  <h2 class="side-title" style="top:950px">CONTACT</h2>
  <div class="contact">
    Street + nr. 12<br>City: &nbsp;Middle Town<br>Postal code: 1612<br>email@address.com<br>Phone Number
  </div>
</aside>

<div class="portrait-ring"><div class="portrait" role="img" aria-label="Portrait photo of the résumé owner"></div></div>

<header class="header">
  <div class="topline"></div>
  <h1 class="name">Your name</h1>
  <div class="profession">Profession</div>
  <div class="contact-line"><span>Email: email@address.com</span><span>Phone Number: 055589655</span></div>
</header>
<div class="rule-h" style="top:176px"></div>
<div class="rule-h" style="top:184px"></div>
<div class="frame-left"></div>
<div class="frame-right"></div>

<svg class="section-icon" style="top:218px" viewBox="0 0 40 36"><rect x="4" y="4" width="32" height="9" fill="var(--wine)"/><rect x="6" y="15" width="28" height="19" fill="var(--wine)"/><rect x="15" y="19" width="10" height="4" fill="#fff"/></svg>
<h2 class="section-title" style="top:222px">WORK EXPERIENCE</h2>

<div class="entry" style="top:273px">
  <div class="dates">2017-2012</div>
  <div class="company-block" role="img" aria-label="Company logo placeholder"></div>
  <div class="body">
    <div class="title">TITLE LOREM &nbsp;SIT DOLOR</div>
    <div class="org">COMPANY NAME</div>
    <div class="desc-label">Description</div>
    <div class="desc">Lorem ipsum dolor sit amet, consectetur adipiscing elit. Proin gravida purus justo, sit amet ultricies turpis aliquam eget. Suspendisse iaculis, lectus at consectetur iaculis, urna ligula imperdiet nisl, a mattis massa dolor vitae quam.</div>
  </div>
</div>
<div class="entry" style="top:430px">
  <div class="dates">2012-2010</div>
  <div class="company-block" role="img" aria-label="Company logo placeholder"></div>
  <div class="body">
    <div class="title">TITLE LOREM &nbsp;SIT DOLOR</div>
    <div class="org">COMPANY NAME</div>
    <div class="desc-label">Description</div>
    <div class="desc">Lorem ipsum dolor sit amet, consectetur adipiscing elit. Proin gravida purus justo, sit amet ultricies turpis aliquam eget. Suspendisse iaculis, lectus at consectetur iaculis, urna ligula imperdiet nisl, a mattis massa dolor vitae quam.</div>
  </div>
</div>
<div class="entry" style="top:587px">
  <div class="dates">2010-2010</div>
  <div class="company-block" role="img" aria-label="Company logo placeholder"></div>
  <div class="body">
    <div class="title">TITLE LOREM &nbsp;SIT DOLOR</div>
    <div class="org">COMPANY NAME</div>
    <div class="desc-label">Description</div>
    <div class="desc">Lorem ipsum dolor sit amet, consectetur adipiscing elit. Proin gravida purus justo, sit amet ultricies turpis aliquam eget. Suspendisse iaculis, lectus at consectetur iaculis, urna ligula imperdiet nisl, a mattis massa dolor vitae quam.</div>
  </div>
</div>

<svg class="section-icon" style="top:757px" viewBox="0 0 40 36"><polygon points="2,10 20,3 38,10 20,17" fill="var(--wine)"/><path d="M9 14 v10 q11 8 22 0 v-10 l-11 5z" fill="var(--wine)"/><rect x="35" y="10" width="2" height="12" fill="var(--wine)"/></svg>
<h2 class="section-title" style="top:760px">EDUCATION</h2>

<div class="entry" style="top:817px">
  <div class="dates">2010-2008</div>
  <div class="body">
    <div class="title">TITLE LOREM &nbsp;SIT DOLOR</div>
    <div class="school">School Name</div>
    <div class="label">Description</div>
    <div class="desc">Lorem ipsum dolor sit amet, consectetur adipiscing elit. Proin gravida purus justo, sit amet ultricies turpis aliquam eget. Suspendisse iaculis</div>
  </div>
</div>
<div class="entry" style="top:934px">
  <div class="dates">2008-2004</div>
  <div class="body">
    <div class="title">TITLE LOREM &nbsp;SIT DOLOR</div>
    <div class="school">School Name</div>
    <div class="label">Description</div>
    <div class="desc">Lorem ipsum dolor sit amet, consectetur adipiscing elit. Proin gravida purus justo, sit amet ultricies turpis aliquam eget. Suspendisse iaculis</div>
  </div>
</div>

<svg class="section-icon" style="top:1058px" viewBox="0 0 40 36"><path d="M2 6 h12 l3 4 h21 v22 h-36z" fill="var(--wine)"/><rect x="14" y="14" width="14" height="14" fill="#fff"/><circle cx="21" cy="19" r="2.5" fill="var(--wine)"/><rect x="17" y="22" width="8" height="5" fill="var(--wine)"/></svg>
<h2 class="section-title" style="top:1058px">ADDITIONAL INFORMATION</h2>
<ul class="extra">
  <li>Vivamus vestibulum nulla nec ante.</li>
  <li>Praesent placerat risus quis eros.</li>
  <li>Fusce pellentesque suscipit nibh.</li>
  <li>Integer vitae libero ac risus egestas placerat.</li>
</ul>
</body>
</html>
```